Solar Billboard Design

We require a billboard 24ftx10ft in size for our solar company.
Artwork Requirement’s:
• Sent on PDF file
• At least 300 dpi
• Scaled to 25% of banner size (24ft x 10ft)
• Please allow at least 40mm space from the artwork edge to allow for any hems and eyelets. This will ensure any important text/images are not cropped/overlapped.
The billboard must have on it:
Solar & Battery Packages
From £8750
In Stock Now!
brightfieldpower.co.uk (must stand out)
________________________
I have attached our logo and some images. I'm not sure if they are good enough quality so you may need to use a stock image.
Kind regards,
Marcus
Target Market(s)
Men & Women aged 35-70, homeowners
Industry/Entity Type
Solar / Construction
Look and feel
Each slider illustrates characteristics of the customer's brand and the style your logo design should communicate.

```html
<!DOCTYPE html>
<html lang="en">
<head>
<meta charset="utf-8">
<title>Solar &amp; Battery Packages Billboard</title>
<link href="https://fonts.googleapis.com/css2?family=Bebas+Neue&display=swap" rel="stylesheet">
<style>
  :root {
    --paper: #ffffff;
    --ink-dark: #454142;
    --band: #454142;
    --band-text: #ffffff;
    --accent-green: #2ec45a;
    --frame-line: #c9c9c9;
    --photo-sky: #9fb0c4;
    --photo-roof: #3c4150;
    --photo-wall: #c9cdd3;
    --photo-grass: #7d9a4e;
  }
  html, body {
    margin: 0;
    padding: 0;
    width: 1200px;
    height: 517px;
    overflow: hidden;
    background: var(--paper);
  }
  .billboard {
    position: relative;
    width: 1200px;
    height: 517px;
    background: var(--paper);
    font-family: "Bebas Neue", "Arial Narrow", sans-serif;
  }
  .trim-frame {
    position: absolute;
    left: 10px;
    top: 11px;
    width: 1180px;
    height: 492px;
    border: 1px solid var(--frame-line);
    box-sizing: border-box;
  }
  .hero-photo {
    position: absolute;
    left: 10px;
    top: 20px;
    width: 603px;
    height: 483px;
    background: linear-gradient(170deg, var(--photo-sky) 0%, var(--photo-grass) 20%, var(--photo-roof) 42%, var(--photo-roof) 62%, var(--photo-wall) 100%);
  }
  .brand-lockup {
    position: absolute;
    left: 800px;
    top: 50px;
    display: flex;
    align-items: center;
    gap: 10px;
    color: var(--ink-dark);
  }
  .brand-mark {
    width: 52px;
    height: 52px;
    border-radius: 50%;
    background: var(--accent-green);
  }
  .brand-name {
    font-size: 21px;
    line-height: 21px;
    letter-spacing: 3px;
  }
  .offer-band {
    position: absolute;
    left: 614px;
    top: 129px;
    width: 566px;
    height: 255px;
    background: var(--band);
    color: var(--band-text);
    text-align: center;
  }
  .offer-title {
    margin: 0;
    position: absolute;
    left: 0;
    right: 0;
    top: 10px;
    font-weight: 400;
    font-size: 82px;
    line-height: 85px;
  }
  .offer-price {
    margin: 0;
    position: absolute;
    left: 0;
    right: 0;
    top: 186px;
    font-size: 73px;
    line-height: 73px;
  }
  .stock-note {
    position: absolute;
    left: 614px;
    width: 566px;
    top: 389px;
    text-align: center;
    font-size: 26px;
    line-height: 26px;
    letter-spacing: 1.5px;
    color: var(--ink-dark);
  }
  .web-address {
    position: absolute;
    left: 614px;
    width: 566px;
    top: 421px;
    text-align: center;
    font-size: 56px;
    line-height: 56px;
    color: var(--accent-green);
    letter-spacing: 0.5px;
  }
</style>
</head>
<body>
  <main class="billboard">
    <div class="trim-frame"></div>
    <div class="hero-photo" role="img" aria-label="Aerial view of a grey house with rooftop solar panels, green fields and mountains behind"></div>

    <div class="brand-lockup">
      <div class="brand-mark"></div>
      <div class="brand-name">Brightfield<br>Energy<br>Group</div>
    </div>

    <section class="offer-band">
      <h1 class="offer-title">Solar &amp; Battery<br>Packages</h1>
      <p class="offer-price">From £8750</p>
    </section>

    <div class="stock-note">In Stock Now!</div>
    <div class="web-address">brightfieldpower.co.uk</div>
  </main>
</body>
</html>
```